Brightwater Array Panel cleaning business needs a flyer designed.

I need a flyer design for a new company based in Los Angeles. We clean solar panels at an affordable price, we're insured, and licensed. we would like the design to include the colors Red, white, and Blue. The flyer should emphasize the importance of cleaning solar panels to maintain the warranty and add longevity to the solar panels.

```html
<!DOCTYPE html>
<html lang="en">
<head>
<meta charset="utf-8">
<title>Brightwater Array Panel Cleaning Flyer</title>
<link href="https://fonts.googleapis.com/css2?family=Archivo+Black&family=Roboto:wght@400;500;700;900&display=swap" rel="stylesheet">
<style>
  :root {
    --red: #c41e2a;
    --blue: #3a3a9e;
    --lavender: #a09ad8;
    --white: #ffffff;
    --ink: #111111;
    --grey: #555555;
  }
  * { margin: 0; padding: 0; box-sizing: border-box; }
  html, body { width: 839px; height: 1200px; overflow: hidden; background: var(--white); }
  .flyer {
    position: relative; width: 839px; height: 1200px; overflow: hidden;
    font-family: "Roboto", Arial, sans-serif; color: var(--ink);
  }
  .backdrop { position: absolute; inset: 0; }
  .brand {
    position: absolute; left: 34px; top: 42px;
    font-family: "Roboto", Arial, sans-serif; font-weight: 900;
    font-size: 27px; letter-spacing: 1px; color: var(--white); text-transform: uppercase;
  }
  .headline {
    position: absolute; left: 47px; top: 256px;
    font-family: "Archivo Black", "Arial Black", sans-serif;
    font-size: 38px; line-height: 46px; letter-spacing: -0.3px;
    color: var(--white); text-transform: uppercase;
  }
  .tagline {
    position: absolute; left: 47px; top: 405px;
    font-size: 19.5px; font-weight: 500; color: var(--white);
  }
  .section-title {
    font-family: "Archivo Black", "Arial Black", sans-serif;
    text-transform: uppercase; line-height: 1.15;
  }
  .why-clean-title { position: absolute; left: 174px; top: 643px; font-size: 23px; color: var(--ink); }
  .item { position: absolute; display: flex; align-items: flex-start; }
  .item .icon {
    width: 42px; height: 42px; border-radius: 50%; flex: none;
    display: flex; align-items: center; justify-content: center;
  }
  .item .icon svg { width: 24px; height: 24px; }
  .item h3 { font-size: 16.5px; font-weight: 500; line-height: 1.2; }
  .item p { font-size: 12.5px; line-height: 1.3; margin-top: 7px; }
  .benefit { left: 26px; width: 400px; }
  .benefit .icon { background: var(--blue); margin-right: 13px; margin-top: 2px; }
  .benefit p { color: var(--grey); }
  .services-title { position: absolute; left: 433px; width: 381px; top: 528px; text-align: center; font-size: 23px; color: var(--white); }
  .service { left: 459px; width: 350px; }
  .service .icon { background: var(--red); margin-right: 13px; margin-top: 2px; }
  .service h3, .service p { color: var(--white); }
  .choose-title { position: absolute; left: 433px; width: 381px; top: 986px; text-align: center; font-size: 23px; color: var(--ink); }
  .perks {
    position: absolute; left: 0; top: 1024px; width: 839px; height: 96px;
    display: grid; grid-template-columns: 407px 1fr; row-gap: 10px; padding: 20px 0 0 26px;
  }
  .perk { display: flex; align-items: center; color: var(--white); font-size: 19.5px; font-weight: 500; }
  .perk svg { width: 17px; height: 17px; margin-right: 12px; flex: none; }
  .cta { position: absolute; left: 28px; top: 1131px; font-size: 23.5px; color: var(--ink); text-transform: none; line-height: 29px; }
  .footer-line { position: absolute; left: 268px; top: 1137px; font-size: 14.5px; color: var(--ink); }
  .contact { position: absolute; left: 268px; top: 1164px; display: flex; align-items: center; font-size: 14.5px; font-weight: 500; color: var(--ink); }
  .contact svg { width: 12px; height: 12px; margin-right: 4px; }
  .contact .sep { margin: 0 12px; }
  .contact span { display: flex; align-items: center; }
</style>
</head>
<body>
<div class="flyer">
  <svg class="backdrop" width="839" height="1200" viewBox="0 0 839 1200">
    <defs>
      <linearGradient id="sky" x1="0" y1="0" x2="0" y2="1">
        <stop offset="0" stop-color="#9aa3ad"/>
        <stop offset="0.45" stop-color="#6f7680"/>
        <stop offset="1" stop-color="#2e3440"/>
      </linearGradient>
    </defs>
    <polygon role="img" aria-label="Photo of two workers in hard hats and safety harnesses cleaning rooftop solar panels with a water-fed brush"
      points="0,0 839,0 839,540 433,523 0,687" fill="url(#sky)"/>
    <polygon points="0,640 433,478 839,468 839,540 433,523 0,687" fill="var(--red)" opacity="0.45"/>
    <polygon points="0,0 554,0 0,240" fill="var(--red)"/>
    <polygon points="0,210 284,105 284,135 0,245" fill="var(--red)" opacity="0.55"/>
    <polygon points="433,523 609,455 814,533 814,969 433,969" fill="var(--blue)"/>
    <rect x="433" y="969" width="381" height="55" fill="var(--lavender)"/>
    <rect x="0" y="1024" width="839" height="96" fill="var(--red)"/>
  </svg>

  <div class="brand">Brightwater Array</div>

  <h1 class="headline">Premium Solar<br>Panel Cleaning<br>Services</h1>
  <p class="tagline">Maximize Your Energy Output &amp; Savings!</p>

  <h2 class="section-title why-clean-title">Why Clean Your<br>Solar Panels?</h2>

  <div class="item benefit" style="top:724px">
    <div class="icon"><svg viewBox="0 0 24 24" fill="none" stroke="#fff" stroke-width="1.6"><circle cx="12" cy="12" r="8"/><path d="M12 7v5l3 3"/></svg></div>
    <div><h3>Boost Efficiency</h3><p>Dirt, dust, and debris reduce energy production by up to 30%</p></div>
  </div>
  <div class="item benefit" style="top:791px">
    <div class="icon"><svg viewBox="0 0 24 24" fill="none" stroke="#fff" stroke-width="1.6"><path d="M19 12a7 7 0 1 1-3-5.7"/><path d="M16 3v4h4"/></svg></div>
    <div><h3>Protect Warranty &amp; Lifespan</h3><p>Keeps your warranty valid and prevents buildup damage for<br>long-term performance</p></div>
  </div>
  <div class="item benefit" style="top:873px">
    <div class="icon"><svg viewBox="0 0 24 24" fill="none" stroke="#fff" stroke-width="1.6"><circle cx="13" cy="9" r="5"/><path d="M3 17l4-2h5l5 3-3 2H7"/></svg></div>
    <div><h3>Save Money</h3><p>More energy means lower electricity bills</p></div>
  </div>
  <div class="item benefit" style="top:941px">
    <div class="icon"><svg viewBox="0 0 24 24" fill="none" stroke="#fff" stroke-width="1.6"><circle cx="12" cy="8" r="4"/><path d="M4 15h16v5H4z"/></svg></div>
    <div><h3>Eco-Friendly Cleaning</h3><p>Safe, non-abrasive, and chemical-free methods</p></div>
  </div>

  <h2 class="section-title services-title">Our Services</h2>

  <div class="item service" style="top:588px">
    <div class="icon"><svg viewBox="0 0 24 24" fill="none" stroke="#fff" stroke-width="1.6"><path d="M5 6h14l2 10H3z"/><path d="M9 6l-1 10M15 6l1 10M4 11h16"/></svg></div>
    <div><h3>Deep Solar Panel Cleaning</h3><p>Removes dust, bird droppings, and grime</p></div>
  </div>
  <div class="item service" style="top:657px">
    <div class="icon"><svg viewBox="0 0 24 24" fill="none" stroke="#fff" stroke-width="1.6"><rect x="5" y="4" width="14" height="16"/><path d="M8 9h8M8 13h8M8 17h5"/></svg></div>
    <div><h3>Regular Maintenance Plans</h3><p>Monthly, quarterly, or annual service options</p></div>
  </div>
  <div class="item service" style="top:726px">
    <div class="icon"><svg viewBox="0 0 24 24" fill="none" stroke="#fff" stroke-width="1.6"><path d="M4 20V9l6-4 6 4v11z"/><circle cx="16" cy="15" r="3"/><path d="M18 17l3 3"/></svg></div>
    <div><h3>Inspection &amp; Performance Check</h3><p>Detects issues before they impact efficiency</p></div>
  </div>
  <div class="item service" style="top:795px">
    <div class="icon"><svg viewBox="0 0 24 24" fill="none" stroke="#fff" stroke-width="1.6"><path d="M4 13h16l-2 7H6z"/><path d="M9 4c-1 2 1 3 0 6M13 4c-1 2 1 3 0 6"/></svg></div>
    <div><h3>Hard Water Stain Removal</h3><p>Prevents long-term damage from mineral<br>buildup</p></div>
  </div>
  <div class="item service" style="top:877px">
    <div class="icon"><svg viewBox="0 0 24 24" fill="none" stroke="#fff" stroke-width="1.6"><path d="M5 20V5h8v15M13 10h6v10M3 20h18"/><path d="M8 8h2M8 12h2M8 16h2"/></svg></div>
    <div><h3>Commercial &amp; Residential Services</h3><p>Custom plans for homes, businesses &amp; solar<br>farms</p></div>
  </div>

  <h2 class="section-title choose-title">Why Choose Us?</h2>

  <div class="perks">
    <div class="perk"><svg viewBox="0 0 20 20"><circle cx="10" cy="10" r="10" fill="#fff"/><path d="M5.5 10.5l3 3 6-6.5" fill="none" stroke="#c41e2a" stroke-width="2.4"/></svg>Licensed, Insured &amp; Trained Pros</div>
    <div class="perk"><svg viewBox="0 0 20 20"><circle cx="10" cy="10" r="10" fill="#fff"/><path d="M5.5 10.5l3 3 6-6.5" fill="none" stroke="#c41e2a" stroke-width="2.4"/></svg>Eco-Friendly &amp; Safe Cleaning Techniques</div>
    <div class="perk"><svg viewBox="0 0 20 20"><circle cx="10" cy="10" r="10" fill="#fff"/><path d="M5.5 10.5l3 3 6-6.5" fill="none" stroke="#c41e2a" stroke-width="2.4"/></svg>Affordable &amp; Flexible Pricing</div>
    <div class="perk"><svg viewBox="0 0 20 20"><circle cx="10" cy="10" r="10" fill="#fff"/><path d="M5.5 10.5l3 3 6-6.5" fill="none" stroke="#c41e2a" stroke-width="2.4"/></svg>100% Satisfaction Guarantee</div>
  </div>

  <h2 class="section-title cta">Call Now for a<br>Free Quote!</h2>
  <p class="footer-line">Brightwater Array Panel &nbsp;– Powering Your Panels for Maximum Efficiency!</p>
  <div class="contact">
    <span><svg viewBox="0 0 12 12"><path d="M6 0a4 4 0 0 1 4 4c0 3-4 8-4 8S2 7 2 4a4 4 0 0 1 4-4z" fill="#c41e2a"/><circle cx="6" cy="4" r="1.5" fill="#fff"/></svg>Los Angeles, CA</span>
    <span class="sep">|</span>
    <span><svg viewBox="0 0 12 12"><path d="M2 1l2.5 0 1 3-1.5 1a7 7 0 0 0 3 3l1-1.5 3 1V10a1 1 0 0 1-1 1C5 11 1 7 1 2a1 1 0 0 1 1-1z" fill="#c41e2a"/></svg>+1 888 555 0142</span>
    <span class="sep">|</span>
    <span><svg viewBox="0 0 12 12"><circle cx="6" cy="6" r="5.5" fill="#c41e2a"/><path d="M1 6h10M6 .5c-2 2.5-2 8.5 0 11M6 .5c2 2.5 2 8.5 0 11" fill="none" stroke="#fff" stroke-width=".8"/></svg>www.brightwaterarray.com</span>
  </div>
</div>
</body>
</html>
```